Three diagrams for an academic paper

I need professional-looking versions of three diagrams for an academic paper. I am uploading JPEGs of each diagram drafted in Vextra Docs. I need completely new versions that look much better.

Some detailed requirements:
- Professional styling - must be clearly superior to the ‘stick-figure’ example images and obviously not from powerpoint, etc.
- Must be a coordinated style across all three illustrations.
- Note that a mini-version of figure 2 appears in figure 3 (within the database image)
- I need very high resolution, suitable for a manuscript
- May need some text changes at short notice (anticipate 2 small updates to text)

Target Market(s)

Academics

Industry/Entity Type

Vextra

Font styles to use
Sans Serif

Colors

Designer to choose colors to be used in the design.

Requirements
Must have
• Don't look like powerpoint

```html
<!DOCTYPE html>
<html lang="en">
<head>
<meta charset="utf-8">
<title>Semiotic Triangle – Reference, Referent, Symbol</title>
<link rel="stylesheet" href="https://fonts.googleapis.com/css2?family=Roboto:wght@300;400;500;700&display=swap">
<style>
  :root {
    --bg: #ffffff;
    --ink: #111418;
    --ink-soft: #3a3f45;
    --band: #eef7f8;
    --node-reference: #d3d7dc;
    --node-referent: #cdedf4;
    --node-symbol: #cfe1e8;
    --inner-line: #b6e1e1;
    --dot-top: #17344e;
    --dot-left: #00a9c8;
    --dot-right: #00668b;
    --art-blue: #1e88d8;
    --art-deep: #0d4f9a;
    --art-grey: #d9dde2;
  }
  * { margin: 0; padding: 0; box-sizing: border-box; }
  html, body { width: 1200px; height: 927px; overflow: hidden; background: var(--bg); }
  .diagram {
    position: relative;
    width: 1200px;
    height: 927px;
    font-family: "Roboto", Arial, sans-serif;
    color: var(--ink);
  }
  .diagram__shapes { position: absolute; inset: 0; }
  .vertex-label {
    position: absolute;
    font-weight: 300;
    font-size: 38px;
    letter-spacing: 0.5px;
    line-height: 1;
    transform: translateY(-50%);
    white-space: nowrap;
  }
  .vertex-label--reference { left: 497px; top: 140px; }
  .vertex-label--referent { left: 197px; top: 642px; }
  .vertex-label--symbol { left: 818px; top: 642px; }

  .relation {
    position: absolute;
    font-weight: 700;
    font-size: 18px;
    letter-spacing: 0.3px;
    white-space: nowrap;
    transform-origin: center;
  }
  .relation--symbolizes { left: 494px; top: 392px; transform: translate(-50%, -50%) rotate(-60deg); }
  .relation--refers { left: 686px; top: 390px; transform: translate(-50%, -50%) rotate(60deg); }
  .relation--stands { left: 589px; top: 561px; transform: translate(-50%, -50%); }

  .definition { position: absolute; white-space: nowrap; }
  .definition__item + .definition__item { margin-top: 10px; }
  .definition__title { font-weight: 500; font-size: 15.5px; line-height: 18px; letter-spacing: 0.2px; }
  .definition__text { font-weight: 300; font-size: 12.6px; line-height: 16px; color: var(--ink-soft); letter-spacing: 0.2px; }
  .definition--reference { left: 725px; top: 176px; }
  .definition--referent { left: 197px; top: 713px; }
  .definition--symbol { left: 819px; top: 721px; }

  .illustration { position: absolute; }
  .illustration--community { left: 230px; top: 298px; width: 144px; height: 144px; border-radius: 50%;
    background: radial-gradient(circle at 45% 40%, #6fc3f5 0%, var(--art-blue) 55%, var(--art-deep) 100%); }
  .illustration--exchange { left: 858px; top: 294px; width: 154px; height: 154px; border-radius: 50%;
    background: radial-gradient(circle, #4aa6e8 0%, #4aa6e8 22%, #eef2f6 23%, var(--art-grey) 100%); }
  .illustration--search { left: 518px; top: 684px; width: 163px; height: 155px; border-radius: 50%;
    background: radial-gradient(circle at 45% 42%, #ffffff 0%, #e3e6ea 45%, #9aa3ad 62%, #1f6fc0 100%); }
</style>
</head>
<body>
<main class="diagram">
  <svg class="diagram__shapes" width="1200" height="927" viewBox="0 0 1200 927" aria-hidden="true">
    <g class="outer-triangle" stroke="var(--band)" stroke-width="28" fill="none" stroke-linejoin="round">
      <polygon points="602,138 310,640 890,640"/>
    </g>
    <circle class="node node--reference" cx="602" cy="138" r="62" fill="var(--node-reference)"/>
    <circle class="node node--referent" cx="310" cy="640" r="62" fill="var(--node-referent)"/>
    <circle class="node node--symbol" cx="890" cy="640" r="62" fill="var(--node-symbol)"/>

    <g class="inner-triangle" stroke="var(--inner-line)" stroke-width="8" fill="none">
      <polygon points="597,302 468,525 724,525"/>
    </g>
    <circle cx="597" cy="302" r="27" fill="var(--dot-top)"/>
    <circle cx="468" cy="525" r="27" fill="var(--dot-left)"/>
    <circle cx="724" cy="525" r="27" fill="var(--dot-right)"/>
  </svg>

  <div class="vertex-label vertex-label--reference">REFERENCE</div>
  <div class="vertex-label vertex-label--referent">REFERENT</div>
  <div class="vertex-label vertex-label--symbol">SYMBOL</div>

  <div class="relation relation--symbolizes">SYMBOLIZES</div>
  <div class="relation relation--refers">REFERS TO</div>
  <div class="relation relation--stands">STANDS FOR</div>

  <div class="definition definition--reference">
    <div class="definition__item">
      <div class="definition__title">FOR NATURAL LANGUAGE</div>
      <div class="definition__text">A CONCEPT IN THE MIND, SHARED WITH A LANGUAGE COMUNITY</div>
    </div>
    <div class="definition__item">
      <div class="definition__title">FOR NATURAL LANGUAGE</div>
      <div class="definition__text">A CONCEPT IN THE MIND, SHARED WITH A LANGUAGE COMUNITY</div>
    </div>
  </div>

  <div class="definition definition--referent">
    <div class="definition__item">
      <div class="definition__title">FOR NATURAL LANGUAGE</div>
      <div class="definition__text">A THING OR CONCEPT IN THE WORLD</div>
    </div>
    <div class="definition__item">
      <div class="definition__title">FOR NATURAL LANGUAGE</div>
      <div class="definition__text">A THING OR CONCEPT IN THE WORLD</div>
    </div>
  </div>

  <div class="definition definition--symbol">
    <div class="definition__item">
      <div class="definition__title">FOR NATURAL LANGUAGE</div>
      <div class="definition__text">WORDS OR PHRASES</div>
    </div>
    <div class="definition__item">
      <div class="definition__title">FOR NATURAL LANGUAGE</div>
      <div class="definition__text">A PATTERN OF SYMBOLS FROM A FINITE SYMBOL SET</div>
    </div>
  </div>

  <div class="illustration illustration--community" role="img" aria-label="Illustration of a group of people in front of a connected globe"></div>
  <div class="illustration illustration--exchange" role="img" aria-label="Illustration of people around a globe linked by circular arrows"></div>
  <div class="illustration illustration--search" role="img" aria-label="Illustration of a magnifying glass over letters A to D with small charts"></div>
</main>
</body>
</html>
```